Fernvale Craft Works business card design- Fine Art sculpture business (Contract guaranteed)

This business card is for a fine art business. Though we don't have a website up and running yet it should be up soon. I would like the business card to be elegant and fairly simple with a picture of one of my sculptures on the front (you might need to photoshop out the background) as well as my basic contact info (my name,phone # and e-mail). On the back I'd like it to be pretty simple with just "Notes" and some blank lines for writing in info.

Target Market(s)

High end artwork buyers

Industry/Entity Type

Art Gallery

Contact Information for Business Card

Marlo Prewitt Phone: (555) 213-4098 E-mail: marlo@quillbrookmail.com Facebook: @fernvalecraftworks Instagram: fernvalecraftworks

Colors

Designer to choose colors to be used in the design.

Requirements
Must have
• *A picture of one of my sculptures*, my name, business name (Fernvale Craft Works), e-mail, phone #, and a notes section on the back.
• Fernvale Craft Works
• Marlo Prewitt
• (555)213-4098
• marlo@quillbrookmail.com
• Facebook: @fernvalecraftworks
• Instagram: fernvalecraftworks
Nice to have
• It'd be nice if you can crop out the background in the sculpture pictures, which ever one you end up using.

```html
<!DOCTYPE html>
<html lang="en">
<head>
<meta charset="utf-8">
<title>Fernvale Craft Works — Business Card</title>
<link href="https://fonts.googleapis.com/css2?family=Source+Sans+3:wght@400;700&family=Arimo:wght@400&display=swap" rel="stylesheet">
<style>
  :root {
    --page: #ffffff;
    --card-base: #dcdde0;
    --card-light: #e6e7ea;
    --card-mist: #c9cdd0;
    --ink: #111111;
    --ink-soft: #1b1b1b;
    --accent: #d9531e;
    --rule: #8a8a8c;
    --line: #23343a;
    --stone-dark: #3a3038;
    --stone-mid: #7a6470;
    --stone-rim: #b8692a;
    --base-dark: #1c1a18;
  }
  html, body {
    margin: 0;
    padding: 0;
    width: 1200px;
    height: 1200px;
    overflow: hidden;
    background: var(--page);
  }
  .canvas {
    position: relative;
    width: 1200px;
    height: 1200px;
    background: var(--page);
  }
  .card-front {
    position: absolute;
    left: 191px;
    top: 133px;
    width: 840px;
    height: 480px;
    background:
      radial-gradient(ellipse 380px 180px at 420px 190px, var(--card-mist), transparent 70%),
      radial-gradient(ellipse 300px 120px at 700px 70px, rgba(255,255,255,0.35), transparent 70%),
      linear-gradient(180deg, var(--card-light) 0%, var(--card-base) 55%, var(--card-light) 100%);
    overflow: hidden;
  }
  .sculpture-photo {
    position: absolute;
    left: 37px;
    top: 37px;
    width: 170px;
    height: 412px;
  }
  .sculpture-photo svg { display: block; width: 100%; height: 100%; }
  .contact {
    position: absolute;
    right: 47px;
    margin: 0;
    text-align: right;
    white-space: nowrap;
    line-height: 1;
    font-family: "Source Sans 3", sans-serif;
    font-size: 29px;
    color: var(--ink-soft);
  }
  .contact-name {
    top: 162px;
    font-weight: 700;
    font-size: 33px;
    color: var(--ink);
  }
  .name-rule {
    position: absolute;
    right: 47px;
    top: 199px;
    width: 140px;
    height: 8px;
    background: var(--rule);
  }
  .contact-company {
    top: 262px;
    font-family: "Arimo", sans-serif;
    font-size: 38px;
    letter-spacing: 1px;
    color: var(--accent);
  }
  .contact-phone { top: 314px; right: 55px; }
  .contact-email { top: 352px; }
  .contact-facebook { top: 390px; }
  .contact-instagram { top: 428px; }
  .notes-label {
    position: absolute;
    left: 244px;
    top: 694px;
    margin: 0;
    font-family: "Arimo", sans-serif;
    font-size: 37px;
    line-height: 1;
    color: var(--ink);
  }
  .notes-lines {
    position: absolute;
    left: 0;
    top: 0;
    width: 1200px;
    height: 1200px;
    pointer-events: none;
  }
</style>
</head>
<body>
<div class="canvas">
  <section class="card-front">
    <div class="sculpture-photo" role="img" aria-label="Photograph of an agate slab sculpture on a dark stone base">
      <svg viewBox="0 0 170 412" preserveAspectRatio="none">
        <defs>
          <linearGradient id="stoneTone" x1="0" y1="0" x2="1" y2="0">
            <stop offset="0" stop-color="var(--stone-rim)"/>
            <stop offset="0.2" stop-color="var(--stone-dark)"/>
            <stop offset="0.6" stop-color="var(--stone-mid)"/>
            <stop offset="1" stop-color="var(--stone-dark)"/>
          </linearGradient>
        </defs>
        <rect x="0" y="0" width="170" height="412" fill="url(#stoneTone)" opacity="0.55"/>
        <rect x="0" y="340" width="170" height="72" fill="var(--base-dark)"/>
      </svg>
    </div>

    <p class="contact contact-name">Marlo Prewitt</p>
    <div class="name-rule"></div>
    <p class="contact contact-company">Fernvale Craft Works</p>
    <p class="contact contact-phone">Phone: (555) 213-4098</p>
    <p class="contact contact-email">E-mail: marlo@quillbrookmail.com</p>
    <p class="contact contact-facebook">Facebook: @fernvalecraftworks</p>
    <p class="contact contact-instagram">Instagram: fernvalecraftworks</p>
  </section>

  <p class="notes-label">Notes:</p>
  <svg class="notes-lines" viewBox="0 0 1200 1200" aria-hidden="true">
    <g stroke="var(--line)" stroke-width="2">
      <line x1="372" y1="726" x2="986" y2="726"/>
      <line x1="244" y1="770" x2="986" y2="770"/>
      <line x1="244" y1="815" x2="986" y2="815"/>
      <line x1="244" y1="859" x2="986" y2="859"/>
      <line x1="244" y1="904" x2="986" y2="904"/>
      <line x1="244" y1="948" x2="986" y2="948"/>
      <line x1="244" y1="993" x2="986" y2="993"/>
    </g>
  </svg>
</div>
</body>
</html>
```